Business Card Velostra - Accounting firm

Hi my friend.
I'm coming back to you to see if it would be possible for you to make a modern and minimalist business card design.
In shades of blue like the great logo you offered me.
The ideal is a modern and aesthetic business card.
The goal is to give a professional effect to the first exchanges.
Renewal and innovation in the accounting world !!
I thank you !!
Good evening to you

Target Market(s)

Young, dynamic and sensitive to marketing

Industry/Entity Type

Finance And Accounting

Contact Information for Business Card

Company logo and name. Last name, First name, Phone number, email address, company address, website.

Font styles to use
Sans Serif

Requirements
Must have
• The ideal is a modern and aesthetic business card.

Mentions to include: Company logo and name. Last name, First name, Phone number, email address, company address, website.
Nice to have
• The goal is to give a professional effect to the first exchanges.
Should not have
• Simplistic or childish design

```html
<!DOCTYPE html>
<html lang="en">
<head>
<meta charset="utf-8">
<title>Velostra Business Card</title>
<link href="https://fonts.googleapis.com/css2?family=Lato:wght@400;700;900&display=swap" rel="stylesheet">
<style>
  :root {
    --navy: #1f2a5e;
    --navy-deep: #19224f;
    --teal: #2fa3c4;
    --teal-light: #4fc1b8;
    --blue: #2c6fd1;
    --white: #ffffff;
    --stage: #e9ebef;
  }
  * { box-sizing: border-box; margin: 0; padding: 0; }
  html, body { width: 1200px; height: 847px; overflow: hidden; }
  body {
    background: var(--stage);
    font-family: "Lato", sans-serif;
    position: relative;
  }
  .card {
    position: absolute;
    width: 525px;
    height: 300px;
    border-radius: 3px;
    box-shadow: 0 14px 30px rgba(20, 30, 60, 0.18);
    overflow: hidden;
  }
  /* Front */
  .card-front {
    left: 50px; top: 90px;
    background: var(--navy);
    border-bottom: 6px solid var(--teal);
  }
  .front-texture {
    position: absolute; inset: 0;
    background: linear-gradient(160deg, #25326b 0%, var(--navy) 55%, var(--navy-deep) 100%);
  }
  .front-brand {
    position: absolute;
    left: 200px; top: 150px;
    display: flex; flex-direction: column;
    color: var(--white);
  }
  .brand-row { display: flex; align-items: center; gap: 10px; }
  .brand-dot {
    width: 22px; height: 22px; border-radius: 50%;
    background: var(--teal-light);
  }
  .brand-name {
    font-weight: 700; font-size: 40px; letter-spacing: 0.5px; line-height: 1;
  }
  .brand-tagline {
    font-size: 9px; letter-spacing: 4px; margin-top: 6px; margin-left: 32px;
  }
  /* Back */
  .card-back {
    left: 625px; top: 460px;
    background: var(--white);
    border-bottom: 6px solid var(--teal);
    color: var(--navy);
  }
  .back-brand {
    position: absolute; right: 36px; top: 38px;
    color: var(--navy);
  }
  .back-brand .brand-dot { background: var(--teal); width: 26px; height: 26px; }
  .back-brand .brand-name { font-size: 42px; }
  .person { position: absolute; left: 36px; top: 50px; }
  .person-name {
    font-weight: 900; font-size: 24px; color: var(--teal); letter-spacing: 0.5px;
  }
  .person-role { font-size: 15px; margin-top: 2px; }
  .divider {
    position: absolute; left: 36px; right: 36px; top: 118px;
    height: 1.5px; background: var(--navy);
  }
  .contacts {
    position: absolute; left: 36px; top: 134px;
    list-style: none; font-size: 15px; line-height: 24px;
  }
  .contacts li { display: flex; align-items: center; gap: 10px; }
  .contacts svg { width: 14px; height: 14px; flex: none; }
  .address {
    position: absolute; right: 36px; bottom: 30px;
    text-align: right; font-size: 16px; line-height: 24px;
  }
</style>
</head>
<body>
  <section class="card card-front">
    <div class="front-texture" role="img" aria-label="Subtle repeating brand pattern on navy"></div>
    <div class="front-brand">
      <div class="brand-row">
        <span class="brand-dot"></span>
        <span class="brand-name">Velostra</span>
      </div>
      <span class="brand-tagline">EXPERT-COMPTABLE</span>
    </div>
  </section>

  <section class="card card-back">
    <div class="person">
      <p class="person-name">JOHN SMITH</p>
      <p class="person-role">Founder &amp; CEO</p>
    </div>
    <div class="back-brand">
      <div class="brand-row">
        <span class="brand-dot"></span>
        <span class="brand-name">Velostra</span>
      </div>
      <span class="brand-tagline" style="display:block;margin-left:36px;">EXPERT-COMPTABLE</span>
    </div>
    <div class="divider"></div>
    <ul class="contacts">
      <li>
        <svg viewBox="0 0 24 24"><path fill="#2fa3c4" d="M6.6 10.8a15 15 0 0 0 6.6 6.6l2.2-2.2c.3-.3.7-.4 1-.2 1.1.4 2.3.6 3.6.6.6 0 1 .4 1 1V20c0 .6-.4 1-1 1C10.6 21 3 13.4 3 4c0-.6.4-1 1-1h3.5c.6 0 1 .4 1 1 0 1.3.2 2.5.6 3.6.1.3 0 .7-.2 1z"/></svg>
        1234567890
      </li>
      <li>
        <svg viewBox="0 0 24 24"><rect x="2" y="5" width="20" height="14" rx="1" fill="#2fa3c4"/><path d="M2 6l10 7 10-7" stroke="#fff" stroke-width="2" fill="none"/></svg>
        info@yourmail.com
      </li>
      <li>
        <svg viewBox="0 0 24 24"><circle cx="12" cy="12" r="9" fill="none" stroke="#2fa3c4" stroke-width="2"/><path d="M3 12h18M12 3c3 3 3 15 0 18M12 3c-3 3-3 15 0 18" fill="none" stroke="#2fa3c4" stroke-width="1.5"/></svg>
        www.yourwebsite.com
      </li>
    </ul>
    <address class="address" style="font-style:normal;">
      1234 First Line Address<br>
      5678 Second Line Address
    </address>
  </section>
</body>
</html>
```